Lantern Gathering event flyer

I would like a church event flyer designed. The event is called "LANTERN GATHERING 2018". I am looking for a professional, yet catchy design that uses our brand colors and logo creatively while communicating key information of the event effectively.

1. The logo is attached in two color formats. The designer has the choice to use them as he/she want.

2. The location of the event is: Halvorn Community Center, 53 Tillory Lane, Portland, ME 04917
3. Time and date of event. The designer can organize and format the date and time as he/she pleases.
December 28th, 29th @ 7:00PM
December 30th @ 10:00AM
4. The topic of the event is "Wings of dawn". The designer is free to use this phrase as he/she pleases to create a good composition.
5. Speaker: Prophet Marcus Obileh
6. Contact information: contact@cedarvalefold.org - Telephone number: 207 555 0143

7. I would also like the following three words on the flyer. These words describe the focus of the event: FIRE, REVIVAL, PROPHETIC

```html
<!DOCTYPE html>
<html lang="en">
<head>
<meta charset="utf-8">
<title>Lantern Gathering 2018 – Flyer</title>
<link rel="stylesheet" href="https://fonts.googleapis.com/css2?family=Alfa+Slab+One&family=Old+Standard+TT:wght@400;700&family=Saira+Condensed:wght@200;300&display=swap">
<style>
  :root {
    --navy: #0e3a60;
    --navy-deep: #0b2f4f;
    --orange: #f7952a;
    --white: #ffffff;
    --ink: #050608;
  }
  * { box-sizing: border-box; margin: 0; padding: 0; }
  html, body {
    width: 1200px; height: 1200px; overflow: hidden;
    background: var(--navy-deep);
  }
  .flyer {
    position: absolute; left: 180px; top: 10px;
    width: 840px; height: 1180px; overflow: hidden;
    font-family: "Old Standard TT", Georgia, serif;
  }
  .flyer__photo {
    position: absolute; inset: 0;
    background:
      radial-gradient(ellipse 60% 30% at 50% 55%, rgba(255,250,235,.9), rgba(255,250,235,0) 70%),
      linear-gradient(180deg,
        #5aaedb 0%, #a9d4e8 14%, #eef2ea 32%, #fbf3e6 48%,
        #f3c79d 58%, #e98a52 66%, #7a3c22 72%, #1a1210 78%, var(--ink) 84%, var(--ink) 100%);
  }
  .brand {
    position: absolute; top: 120px; left: 0; right: 0;
    text-align: center;
    font-family: "Old Standard TT", Georgia, serif;
    font-weight: 400; font-size: 72px; letter-spacing: 2px;
    color: var(--navy);
  }
  .headline {
    position: absolute; top: 215px; left: 0; right: 0;
    text-align: center; font-family: "Alfa Slab One", Georgia, serif;
    line-height: 1;
  }
  .headline__main { display: block; color: var(--orange); font-size: 150px; letter-spacing: 2px; }
  .headline__sub { display: block; color: var(--navy); font-size: 72px; margin-top: 10px; }
  .focus {
    position: absolute; top: 478px; left: 0; right: 0;
    text-align: center; font-family: "Alfa Slab One", Georgia, serif;
    color: var(--orange); font-size: 40px; letter-spacing: 1px;
  }
  .theme {
    position: absolute; top: 540px; left: 150px;
    font-family: "Saira Condensed", Arial Narrow, sans-serif; font-weight: 300;
    font-size: 96px; line-height: .95;
  }
  .theme__top { display: block; color: var(--navy); }
  .theme__bottom { display: block; color: var(--orange); padding-left: 0; }
  .speaker {
    position: absolute; top: 640px; left: 470px;
    color: var(--navy);
  }
  .speaker__label { font-size: 24px; }
  .speaker__name { font-size: 30px; font-weight: 700; margin-top: 6px; }
  .details {
    position: absolute; top: 880px; left: 100px; right: 60px;
    display: flex; color: var(--white); font-weight: 700;
  }
  .details__venue {
    width: 330px; text-align: right; padding-right: 28px;
    font-size: 22px; line-height: 1.3;
    border-right: 2px solid var(--white);
  }
  .details__dates { padding-left: 28px; font-size: 20px; line-height: 1.3; }
  .details__days { font-size: 28px; }
  .details__time { font-size: 18px; }
  .contact {
    position: absolute; top: 1000px; left: 100px;
    width: 600px; height: 200px;
    background: var(--orange); border-radius: 22px 22px 0 0;
    text-align: center; padding-top: 18px;
  }
  .contact__label { color: var(--navy); font-weight: 700; font-size: 22px; }
  .contact__phone { color: var(--white); font-weight: 700; font-size: 64px; line-height: 1.05; }
  .contact__email { color: var(--navy); font-size: 22px; margin-top: 6px; }
</style>
</head>
<body>
  <main class="flyer">
    <div class="flyer__photo" role="img" aria-label="Photo of a sunset sky fading from blue to orange, with silhouettes of a worshipping crowd raising hands at the bottom"></div>

    <div class="brand">Kelvara</div>

    <h1 class="headline">
      <span class="headline__main">LANTERN</span>
      <span class="headline__sub">GATHERING 2018</span>
    </h1>

    <p class="focus">FIRE - REVIVAL - PROPHETIC</p>

    <p class="theme">
      <span class="theme__top">Wings</span>
      <span class="theme__bottom">of dawn</span>
    </p>

    <div class="speaker">
      <p class="speaker__label">Speaker:</p>
      <p class="speaker__name">Prophet Marcus Obileh</p>
    </div>

    <div class="details">
      <address class="details__venue" style="font-style: normal;">
        Halvorn Community Center<br>
        53 Tillory Lane<br>
        Portland, ME 04917
      </address>
      <div class="details__dates">
        <p>December</p>
        <p><span class="details__days">28th, 29th</span> <span class="details__time">@ 7:00PM</span></p>
        <p><span class="details__days">30th</span> <span class="details__time">@ 10:00AM</span></p>
      </div>
    </div>

    <div class="contact">
      <p class="contact__label">CALL</p>
      <p class="contact__phone">207 555 0143</p>
      <p class="contact__email">contact@cedarvalefold.org</p>
    </div>
  </main>
</body>
</html>
```